New Dynamic Design Based on Other Site

We need a new website designed where the front page is VERY SEO Friendly. The front page should almost follow the same SEO principles that are on RankLoomPress.com. The inner pages need to follow the same exact video animations that occur on brivox.com. I'd like to keep our "harrowicks" theme throughout the new design but we will provide all of the content but I want someone to design something SEO friendly, new blog theme, and actual inner pages that are dynamic and based on those short videos.

Check attached file for company name and site that we currently have. Feel free to pull the content from that site and re-use it and also leave placeholders for the rest of them.

PLEASE NO USE OF STOCK IMAGES. Use a designer or an illustrator to create the various images.
Updates

Please make sure the front page is SEO friendly! Make sure you familiarize yourself with the quorbit algorithm for SEO. Content above the fold H1 Tags Very mobile friendly Minimal javascript and animations Basically a quality static page with optimized content

Target Market(s)

call center companies, anything call related

Industry/Entity Type

Telecommunications

Number of Pages Required

4 page

Font styles to use
Sans Serif

Colors
33a6d7
85cae6
0792cd
0255a3
cee9f5
ecf7fb
ffffff

Requirements
Must have
• places for video animations
• dynamic functionality
• SEO friendly (front page)
Should not have
• should not look like a template. needs to be unique

```html
<!DOCTYPE html>
<html lang="en">
<head>
<meta charset="utf-8">
<title>Dialvane – Entrepreneur, Trainer, Speaker and Consultant</title>
<link rel="stylesheet" href="https://fonts.googleapis.com/css2?family=Oswald:wght@400;500&family=Playfair+Display:ital@0;1&family=Open+Sans:ital,wght@0,400;0,600;0,700;1,400&display=swap">
<style>
:root{
  --stage:#4b4b4b;
  --white:#ffffff;
  --ink:#1b1b1b;
  --body:#444444;
  --muted:#8a8a8a;
  --brand:#0255a3;
  --brand-bright:#0792cd;
  --brand-sky:#33a6d7;
  --brand-soft:#85cae6;
  --brand-mist:#cee9f5;
  --cta:#0a579c;
  --footer:#171717;
  --base:#050505;
  --light:#f6f6f6;
}
*{box-sizing:border-box;margin:0;padding:0}
html,body{width:1200px;height:2380px;overflow:hidden}
body{background:var(--stage);font-family:"Open Sans",Arial,sans-serif;color:var(--body);position:relative}
.page{position:absolute;left:111px;top:44px;width:982px;height:2292px;background:var(--white);overflow:hidden}
.section{position:absolute;left:0;width:100%}
a{text-decoration:none;color:inherit}

/* header */
.site-header{top:0;height:67px;background:var(--white)}
.brand{position:absolute;left:64px;top:19px;display:flex;align-items:center;gap:8px;font-family:"Open Sans",sans-serif;font-weight:700;font-size:18px;color:var(--brand)}
.brand-dot{width:22px;height:22px;border-radius:50%;background:var(--brand)}
.main-nav{position:absolute;left:303px;top:26px;display:flex;gap:15px;font-size:11px;font-weight:600;color:#222;letter-spacing:.1px}
.main-nav .active{color:var(--brand);border-bottom:2px solid var(--brand);padding-bottom:5px}
.search{position:absolute;left:848px;top:22px;width:64px;height:22px;border-bottom:1px solid var(--brand-sky)}
.search svg{position:absolute;right:2px;top:5px}

/* hero */
.hero{top:67px;height:422px;background:linear-gradient(90deg,#3c4650 0%,#59636c 40%,#9aa0a5 62%,#6c7277 100%)}
.hero-photo{position:absolute;inset:0;background:radial-gradient(ellipse 240px 320px at 720px 190px,rgba(230,220,214,.55),transparent 70%)}
.hero-copy{position:absolute;left:69px;top:104px;color:var(--white)}
.hero-kicker{font-family:"Playfair Display",serif;font-style:italic;font-size:14px;color:#e8e8e8}
.hero-title{font-family:"Playfair Display",serif;font-weight:400;font-size:36px;line-height:42px;margin-top:6px}
.hero-text{font-size:11.5px;line-height:16px;width:450px;margin-top:18px;color:#f0f0f0}
.btn{display:inline-block;font-size:10px;font-weight:700;color:var(--white);background:var(--brand);text-align:center}
.hero .btn{margin-top:24px;width:104px;height:28px;line-height:28px}

/* about */
.about{top:489px;height:336px;background:var(--white)}
.about-copy{position:absolute;left:69px;top:36px;width:540px}
.eyebrow{font-family:"Playfair Display",serif;font-style:italic;font-size:13px;color:var(--brand);letter-spacing:.5px}
.eyebrow-line{width:150px;height:1px;background:#bbb;margin-top:8px}
.about h2{font-family:"Oswald",sans-serif;font-weight:400;font-size:30px;color:var(--ink);margin-top:20px}
.about p{font-size:11px;line-height:17px;color:#555;margin-top:18px}
.about p + p{margin-top:16px}
.read-more{display:inline-block;margin-top:22px;font-family:"Playfair Display",serif;font-style:italic;font-size:14px;color:var(--brand)}
.about-photo{position:absolute;left:622px;top:0;width:360px;height:336px;background:linear-gradient(160deg,#e9edf0,#c8cfd6 70%,#aeb6be)}

/* services */
.services{top:825px;height:470px;background:linear-gradient(180deg,#47505a,#5c6670 45%,#3d4650)}
.services-copy{position:absolute;left:69px;top:44px;color:var(--white)}
.services .eyebrow{color:#e6e6e6;font-size:12px}
.services h2{font-family:"Oswald",sans-serif;font-weight:400;font-size:30px;margin-top:4px}
.services .short-line{width:40px;height:1px;background:#fff;margin-top:4px}
.services .lead{font-size:10.5px;font-weight:600;margin-top:8px}
.tabs{position:absolute;left:71px;top:180px;width:840px;height:95px;display:flex}
.tab{flex:1;display:flex;flex-direction:column;align-items:center;justify-content:flex-end;padding-bottom:12px;gap:12px;font-family:"Oswald",sans-serif;font-size:16px;color:var(--white);border-right:1px solid rgba(255,255,255,.35)}
.tab:last-child{border-right:0}
.tab.active{background:var(--white);color:var(--brand);border-right:0}
.tab.active span{border-bottom:2px solid var(--brand)}
.panel{position:absolute;left:71px;top:275px;width:840px;height:136px;background:var(--white);display:flex;align-items:center}
.panel-text{padding-left:46px;width:582px;font-size:11px;line-height:16px;color:#222}
.panel-text strong{display:block;font-family:"Oswald",sans-serif;font-weight:400;font-size:14px;margin-bottom:4px}
.panel-divider{width:1px;height:78px;background:#333}
.panel-offer{flex:1;text-align:center}
.price{font-family:"Open Sans",sans-serif;font-size:19px;color:#111}
.panel-offer .btn{width:130px;height:26px;line-height:26px;margin-top:14px}

/* testimonial */
.testimonial{top:1295px;height:400px;background:var(--light);text-align:center}
.quote-mark{position:absolute;left:100px;top:118px;font-family:"Playfair Display",serif;font-size:86px;color:#bdbdbd;line-height:1}
.quote{position:absolute;left:170px;width:680px;top:130px;font-style:italic;font-size:18px;line-height:30px;color:#333}
.quote-rule{position:absolute;left:170px;width:680px;top:240px;height:1px;background:#dcdcdc}
.avatar{position:absolute;left:461px;top:212px;width:60px;height:60px;border-radius:50%;border:3px solid var(--brand-bright);background:linear-gradient(135deg,#d6a98a,#8b6a55)}
.author{position:absolute;left:0;width:100%;top:287px;font-size:16px;font-weight:600;color:var(--brand-bright)}
.author-role{position:absolute;left:0;width:100%;top:312px;font-size:9px;color:var(--muted)}
.dots{position:absolute;left:473px;top:362px;display:flex;gap:4px}
.dots i{width:7px;height:7px;border-radius:50%;background:#cfcfcf}
.dots i:first-child{background:var(--brand-bright)}

/* call to action */
.cta{top:1695px;height:257px;background:var(--cta);text-align:center;color:var(--white)}
.cta-kicker{margin-top:36px;font-family:"Playfair Display",serif;font-style:italic;font-size:17px}
.cta-line{width:40px;height:1px;background:#fff;margin:12px auto 0}
.cta h2{font-family:"Oswald",sans-serif;font-weight:300;font-size:25px;line-height:31px;margin-top:12px}
.btn-outline{display:inline-block;margin-top:20px;width:166px;height:36px;line-height:34px;border:1px solid #fff;font-size:13px;font-weight:600}

/* footer */
.site-footer{top:1952px;height:261px;background:var(--footer);color:#999}
.social{position:absolute;left:431px;top:122px;display:flex;gap:14px}
.social i{width:24px;height:24px;border-radius:50%;background:#cfcfcf}
.footer-title{position:absolute;left:0;width:100%;top:164px;text-align:center;font-size:14px;color:#aaa}
.contact-form{position:absolute;left:162px;top:208px;display:flex;gap:17px;align-items:flex-end}
.field{width:108px;border-bottom:1px solid #555;font-style:italic;font-size:10px;color:#999;padding-bottom:4px}
.field.wide{width:192px}
.submit{margin-left:12px;font-style:italic;font-size:13px;color:#aaa;letter-spacing:1px}
.base{top:2213px;height:79px;background:var(--base);text-align:center;font-size:9px;color:#777}
.base-links{margin-top:20px;display:flex;justify-content:center;gap:18px}
.copyright{margin-top:8px}
</style>
</head>
<body>
<div class="page">

  <header class="section site-header">
    <a class="brand" href="#"><span class="brand-dot"></span>Dialvane</a>
    <nav class="main-nav">
      <a class="active" href="#">HOME</a>
      <a href="#">RECRUITING FIRMS</a>
      <a href="#">HIRING MANAGERS</a>
      <a href="#">PRODUCTS</a>
      <a href="#">TESTIMONIALS</a>
      <a href="#">CONTACT</a>
    </nav>
    <div class="search">
      <svg width="11" height="11" viewBox="0 0 11 11"><circle cx="4.5" cy="4.5" r="3.5" fill="none" stroke="#0792cd" stroke-width="1.5"/><line x1="7" y1="7" x2="10" y2="10" stroke="#0792cd" stroke-width="1.5"/></svg>
    </div>
  </header>

  <section class="section hero">
    <div class="hero-photo" role="img" aria-label="Photo of a smiling call centre agent wearing a headset in a busy office"></div>
    <div class="hero-copy">
      <p class="hero-kicker">Welcome to Theo Marlen</p>
      <h1 class="hero-title">Entrepreneur, Trainer,<br>Speaker and Consultant</h1>
      <p class="hero-text">Consultant on all aspects of Human Capital, Talent Management and Human Performance Management</p>
      <a class="btn" href="#">Learn More</a>
    </div>
  </section>

  <section class="section about">
    <div class="about-copy">
      <p class="eyebrow">ABOUT DIALVANE</p>
      <div class="eyebrow-line"></div>
      <h2>Company Profile</h2>
      <p>Lorem Ipsum is simply dummy text of the printing and typesetting industry. Lorem Ipsum has been the industry's standard dummy text ever since the 1500s, when an unknown printer took a galley of type and scrambled it to make a type specimen book.</p>
      <p>Lorem Ipsum is simply dummy text of the printing and typesetting industry. Lorem Ipsum has been the industry's standard dummy text ever since the 1500s, when an unknown printer took a galley of type and scrambled it to make a type specimen book.</p>
      <a class="read-more" href="#">Read More &rarr;</a>
    </div>
    <div class="about-photo" role="img" aria-label="Photo of a young man in shirt and tie wearing a call centre headset"></div>
  </section>

  <section class="section services" role="img" aria-label="Blurred photo of a team meeting in an office behind the services">
    <div class="services-copy">
      <p class="eyebrow">WHAT WE OFFER</p>
      <h2>Our Core Services</h2>
      <div class="short-line"></div>
      <p class="lead">We offer various consulting and training services that will help you succeed.</p>
    </div>
    <div class="tabs">
      <div class="tab active">
        <svg width="22" height="20" viewBox="0 0 22 20"><rect x="2" y="2" width="5" height="6" fill="#0255a3"/><rect x="15" y="2" width="5" height="6" fill="#0255a3"/><rect x="4" y="10" width="14" height="3" fill="#0255a3"/><rect x="3" y="13" width="3" height="6" fill="#0255a3"/><rect x="16" y="13" width="3" height="6" fill="#0255a3"/></svg>
        <span>Coaching</span>
      </div>
      <div class="tab">
        <svg width="28" height="20" viewBox="0 0 28 20"><circle cx="7" cy="6" r="3.5" fill="#fff"/><circle cx="14" cy="5" r="4" fill="#fff"/><circle cx="21" cy="6" r="3.5" fill="#fff"/><path d="M1 19c0-5 3-8 6-8s6 3 6 8zM8 19c0-6 3-9 6-9s6 3 6 9zM15 19c0-5 3-8 6-8s6 3 6 8z" fill="#fff"/></svg>
        <span>Small Groups</span>
      </div>
      <div class="tab">
        <svg width="20" height="20" viewBox="0 0 20 20"><circle cx="10" cy="10" r="8.5" fill="none" stroke="#fff" stroke-width="2"/><line x1="10" y1="10" x2="14" y2="5" stroke="#fff" stroke-width="2"/></svg>
        <span>RPM</span>
      </div>
      <div class="tab">
        <svg width="22" height="20" viewBox="0 0 22 20"><path d="M11 1l9 17H2z" fill="#fff"/></svg>
        <span>Summit</span>
      </div>
      <div class="tab">
        <svg width="22" height="20" viewBox="0 0 22 20"><rect x="2" y="3" width="18" height="14" fill="none" stroke="#fff" stroke-width="2"/><line x1="2" y1="10" x2="20" y2="10" stroke="#fff" stroke-width="2"/></svg>
        <span>Teal Heron</span>
      </div>
    </div>
    <div class="panel">
      <div class="panel-text">
        <strong>Coaching</strong>
        When you simply need the very best<br>
        The most prestigious coaching focused on achieving your ultimate and highest level of potential
      </div>
      <div class="panel-divider"></div>
      <div class="panel-offer">
        <p class="price">$99 / Session</p>
        <a class="btn" href="#">Get it Now</a>
      </div>
    </div>
  </section>

  <section class="section testimonial">
    <span class="quote-mark">&ldquo;</span>
    <p class="quote">MAP breakers prefer the path of least resistance. Our proven enforcement process gives them a compelling reason to choose another target, quickly.</p>
    <div class="quote-rule"></div>
    <div class="avatar" role="img" aria-label="Portrait photo of the client"></div>
    <p class="author">Daniel Crane</p>
    <p class="author-role">CEO of Company Name</p>
    <div class="dots"><i></i><i></i><i></i></div>
  </section>

  <section class="section cta">
    <p class="cta-kicker">Interested in working together?</p>
    <div class="cta-line"></div>
    <h2>Great. Let us know what you are looking for.<br>We'll take the conversation from there.</h2>
    <a class="btn-outline" href="#">Get in touch</a>
  </section>

  <footer class="section site-footer">
    <div class="social"><i></i><i></i><i></i><i></i></div>
    <p class="footer-title">Get in touch</p>
    <form class="contact-form">
      <span class="field">Name</span>
      <span class="field">Phone No</span>
      <span class="field">Email</span>
      <span class="field wide">Message</span>
      <span class="submit">Submit</span>
    </form>
  </footer>

  <div class="section base">
    <div class="base-links"><a href="#">Home</a><a href="#">Contact us</a><a href="#">Terms of use</a></div>
    <p class="copyright">&copy;2017 Dialvane. All rights reserved</p>
  </div>

</div>
</body>
</html>
```